Progressive business consultancy seeking innovative and clever powerpoint design

Were looking for a PowerPoint design for our Melbourne based business consulting company, Fenwo-x.

About Us:
Based in Melbourne, Australia, Fenwo-x is a management consulting organisation that partners with their clients to lead the execution of strategic process and system improvement initiatives.

Fenwo-x offers business advisory services in Project Management, Business Process Management, Change Management, Business Analysis and Business Intelligence. Fenwo-x combines hands on delivery with coaching in best practice methodologies and approaches to build our clients capabilities ensuring their ongoing success in project implementations.

Fenwo-x has extensive experience across a wide range of industries. We specialise in assisting organisations across the accounting, legal, financial services and health sectors.

Our core purpose is to help businesses in the middle market navigate transformational change through clear and focused execution and enablement.

www.fenwo-x.com.au
@fenwo_x

What we're looking for:
A PowerPoint template consisting of:
- a front/cover page with hero image (attached)
- a contents page
- a divider page (for different segments of the slide deck)
- a standard PowerPoint content page
- a blank PowerPoint page. (still Fenwo-x themed)

The Fenwo-x colours are white and blue (RGB:0/86/162 and
CMYK 97/73/4/0)

All slides should have the Fenwo-x logo (attached) and a professional, almost corporate, (but not boring) theme that is consistent across all slides. The design should reflect our focus on the "e" in fenwo-x, which is what we're really about - "e"xecution and "e"nablement of change.

I've attached a PNG file of our word template which shows the focus on the "e" as a watermark on the document as well as the font files if required.

Let me know if you need any further information or design specifics.

Thanks,

Delphine
(on behalf of Gregory)

Reason: Hi Designers, We have received some really great designs. Thanks for taking the time to make your submissions. We have decided to extend the deadline as we need some more time to review and consult other colleagues on the great submissions we have received. We are also hoping we might get some additional submissions over the weekend. We would also like enough time to provide feedback on all the submissions received. Thanks for helping us out with some really creative work. Gregory @fenwo_x

Reason: Hi designers, thanks for taking the time to submit your designs. We have some really great submissions. We are going to have to extend our deadline again as we just haven't had the chance to review and provide feedback on all the designs. We will be closing this project off on Tuesday March 17. Thanks Gregory @fenwo_x

Target Market(s)

C-Level executives (CEO,COO,CIO) at professional services firms (Accounting and Legal), not for profit organisations and financial services firms.

Industry/Entity Type

Management Consulting

Font styles to use
Serif
Other font styles liked:
• Calibri or attached fonts

Requirements
Must have
• A PowerPoint template consisting of:
• 1) a front/cover page with hero image (attached)
• 2) a contents page
• 3) a divider page (for different segments of the slide deck)
• 4) a standard PowerPoint content page
• 5) a blank PowerPoint page. (still Fenwo-x themed)
• 6) Two content
• 7) Comparison
• 8) Table
• 9) Picture column
• 10) Chevron
• The Fenwo-x colours are white and blue (RGB:0/86/162 and
• CMYK 97/73/4/0)

```html
<!DOCTYPE html>
<html lang="en">
<head>
<meta charset="utf-8">
<title>Fenwo-x slide template – two container and table pages</title>
<link rel="stylesheet" href="https://fonts.googleapis.com/css2?family=Exo+2:wght@300;400&display=swap">
<style>
  :root {
    --brand-blue: #0056a2;
    --ink: #1d1d1d;
    --paper: #ffffff;
    --backdrop: #e9e9e9;
    --cell-border: #0056a2;
  }
  * { box-sizing: border-box; margin: 0; padding: 0; }
  html, body { width: 849px; height: 1200px; overflow: hidden; }
  body {
    background: var(--backdrop);
    font-family: "Exo 2", sans-serif;
    font-weight: 300;
    color: var(--ink);
    position: relative;
  }
  .slide {
    position: absolute;
    background: var(--paper);
    box-shadow: 0 2px 6px rgba(0,0,0,0.15);
  }
  .slide--two-container { left: 64px; top: 61px; width: 709px; height: 532px; }
  .slide--table { left: 71px; top: 610px; width: 702px; height: 526px; }

  .slide-title {
    position: absolute;
    font-size: 22px;
    font-weight: 300;
    letter-spacing: -0.2px;
    white-space: nowrap;
  }
  .slide-title .accent { color: var(--brand-blue); }
  .slide--two-container .slide-title { left: 43px; top: 52px; }
  .slide--table .slide-title { left: 42px; top: 51px; }

  .brand-name {
    position: absolute;
    right: 36px;
    top: 56px;
    color: var(--ink);
    font-size: 17px;
    font-weight: 300;
    letter-spacing: 3px;
    text-transform: uppercase;
  }

  .column {
    position: absolute;
    top: 128px;
    font-size: 13.6px;
    line-height: 19px;
    text-align: justify;
  }
  .column p + p { margin-top: 19px; }
  .column--left { left: 48px; width: 264px; }
  .column--right { left: 362px; width: 300px; }

  .page-number {
    position: absolute;
    right: 20px;
    bottom: 12px;
    font-size: 17px;
    font-weight: 400;
  }

  .step-table {
    position: absolute;
    left: 43px;
    top: 100px;
    display: grid;
    grid-template-columns: 181px repeat(4, 101px);
    grid-template-rows: 58px repeat(5, 41px);
    column-gap: 4px;
    row-gap: 4px;
  }
  .cell {
    display: flex;
    align-items: center;
    justify-content: center;
    border-radius: 6px;
    font-size: 16px;
  }
  .cell--head, .cell--label {
    background: var(--brand-blue);
    color: #fff;
    font-weight: 400;
    font-size: 16.5px;
  }
  .cell--value {
    background: var(--paper);
    border: 2px solid var(--cell-border);
    color: #111;
    font-weight: 400;
    font-size: 15px;
  }

  .table-caption {
    position: absolute;
    left: 40px;
    right: 40px;
    top: 397px;
    text-align: center;
    font-size: 14.5px;
    line-height: 20.5px;
  }
</style>
</head>
<body>

<section class="slide slide--two-container">
  <h2 class="slide-title">TWO <span class="accent">CONTAINER PAGE</span></h2>
  <span class="brand-name">Fenwo-x</span>

  <div class="column column--left">
    <p>Based in Melbourne, Australia, Fenwo-x is a management consulting organisation who partner with their clients to lead the execution of strategic process and system improvement initiatives. Our core purpose is to help your business navigate transformational change through clear and focused execution and enablement.</p>
    <p>Our Melbourne based office includes a range of professional management consulting services from business analysis, business intelligence, project management,</p>
  </div>

  <div class="column column--right">
    <p>Based in Melbourne, Australia, Fenwo-x is a management consulting organisation who partner with their clients to lead the execution of strategic process and system improvement initiatives. Our core purpose is to help your business navigate transformational change through clear and focused execution and enablement.</p>
    <p>Our Melbourne based office includes a range of professional management consulting services from business analysis, business intelligence, project management, business process management and change management.</p>
  </div>

  <span class="page-number">04</span>
</section>

<section class="slide slide--table">
  <h2 class="slide-title">YOUR COMPANY <span class="accent">TABLES COMES HERE</span></h2>
  <span class="brand-name">Fenwo-x</span>

  <div class="step-table" role="table">
    <div class="cell cell--head">Name of the sub title</div>
    <div class="cell cell--head">STEP 01</div>
    <div class="cell cell--head">STEP 02</div>
    <div class="cell cell--head">STEP 03</div>
    <div class="cell cell--head">STEP 04</div>

    <div class="cell cell--label">INSERT YOUR TEXT</div>
    <div class="cell cell--value">01</div>
    <div class="cell cell--value">02</div>
    <div class="cell cell--value">02</div>
    <div class="cell cell--value">08</div>

    <div class="cell cell--label">INSERT YOUR TEXT</div>
    <div class="cell cell--value">06</div>
    <div class="cell cell--value">01</div>
    <div class="cell cell--value">03</div>
    <div class="cell cell--value">01</div>

    <div class="cell cell--label">INSERT YOUR TEXT</div>
    <div class="cell cell--value">10</div>
    <div class="cell cell--value">04</div>
    <div class="cell cell--value">08</div>
    <div class="cell cell--value">06</div>

    <div class="cell cell--label">INSERT YOUR TEXT</div>
    <div class="cell cell--value">08</div>
    <div class="cell cell--value">09</div>
    <div class="cell cell--value">09</div>
    <div class="cell cell--value">08</div>

    <div class="cell cell--label">INSERT YOUR TEXT</div>
    <div class="cell cell--value">05</div>
    <div class="cell cell--value">08</div>
    <div class="cell cell--value">07</div>
    <div class="cell cell--value">09</div>
  </div>

  <p class="table-caption">Based in Melbourne, Australia, Fenwo-x is a management consulting organisation<br>who partner with their clients to lead the execution of strategic process and<br>system improvement initiatives.</p>

  <span class="page-number">05</span>
</section>

</body>
</html>
```